martial arts school needs a flyer to attract new starters in wing chun kung fu

we need a flyer design to be sent out in the local community to attract new customers to our martial arts school. we intend to run introduction classes for begineers. the design should be attractive to new starters looking to get fit - learn a martial art - make new friends - improve self confidence.
also the flyer should say "free class with this flyer" . we also need big poster to put up around the local area
Updates

the following dress should be on the design Aire Valley Martial ArtsGround FloorThe MillGreengage RoadKeighleyBD21 5LH Added Sunday, April 5, 2015

contact telephone number on the design ; 079 46081 572 Added Sunday, April 5, 2015

Industry/Entity Type

School

Requirements
Must have
• it must say - wing chun kung fu classes - introduction classes -

```html
<!DOCTYPE html>
<html lang="en">
<head>
<meta charset="utf-8">
<title>Wing Chun Kung Fu Classes – Flyer</title>
<link rel="stylesheet" href="https://fonts.googleapis.com/css2?family=Anton&family=Archivo+Black&family=Oswald:wght@600&family=Arimo:wght@400;700&display=swap">
<style>
  :root {
    --red: #e8202f;
    --navy: #14214a;
    --ink: #111111;
    --blue: #1d5ba6;
    --yellow: #fff200;
    --paper: #ffffff;
    --stage: #ffffff;
    --gi: #e9ecef;
    --gi-shade: #c9ced4;
  }
  * { margin: 0; padding: 0; box-sizing: border-box; }
  html, body { width: 1200px; height: 1000px; overflow: hidden; background: var(--stage); }
  .canvas { position: relative; width: 1200px; height: 1000px; }

  .flyer {
    position: absolute;
    background: var(--paper);
    overflow: hidden;
    font-family: "Arimo", Arial, sans-serif;
  }
  .flyer--classic { left: 30px; top: 95px; width: 618px; height: 875px; border: 2px solid var(--ink); box-shadow: 4px 4px 10px rgba(0,0,0,.35); }
  .flyer--modern { left: 668px; top: 215px; width: 510px; height: 745px; box-shadow: 4px 4px 10px rgba(0,0,0,.35); }

  .photo { position: absolute; }
  .photo--instructor { left: 0; top: 0; width: 270px; height: 680px;
    background: linear-gradient(180deg, #ece8e4 0%, var(--gi) 30%, var(--gi-shade) 100%); border-radius: 0 120px 0 0; }
  .photo--pair { left: 235px; top: 205px; width: 275px; height: 330px;
    background: linear-gradient(180deg, #f2efec 0%, var(--gi) 45%, var(--gi-shade) 100%); border-radius: 90px 90px 0 0; }

  .title { position: absolute; font-family: "Anton", Impact, sans-serif; color: var(--red); line-height: 1; white-space: nowrap; transform-origin: left top; }
  .subtitle { position: absolute; font-family: "Archivo Black", Arial, sans-serif; color: var(--navy); line-height: 1; white-space: nowrap; }
  .rule { position: absolute; height: 2px; background: var(--navy); }
  .intro { position: absolute; font-family: "Arimo", Arial, sans-serif; font-weight: 700; color: var(--ink); line-height: 1; white-space: nowrap; }

  .flyer--classic .title { left: 192px; top: 50px; font-size: 80px; letter-spacing: 1px; transform: scaleX(1.18); }
  .flyer--classic .subtitle { left: 192px; top: 136px; font-size: 31px; letter-spacing: 3px; }
  .flyer--classic .rule { left: 215px; top: 183px; width: 403px; }
  .flyer--classic .intro { left: 225px; top: 190px; font-size: 24px; }

  .school-mark { position: absolute; display: flex; align-items: center; gap: 10px; }
  .school-mark__dot { width: 22px; height: 22px; border-radius: 50%; background: var(--navy); flex: none; }
  .school-mark__name { font-family: "Arimo", Arial, sans-serif; font-weight: 700; color: var(--navy); line-height: 1.15; }
  .flyer--classic .school-mark { left: 315px; top: 318px; width: 200px; }
  .flyer--classic .school-mark__name { font-size: 20px; }

  .benefits { position: absolute; text-align: right; transform: rotate(-4deg); transform-origin: right bottom; white-space: nowrap; }
  .benefits li { list-style: none; line-height: 1.1; }
  .flyer--classic .benefits { right: 28px; top: 462px; font-family: "Archivo Black", Arial, sans-serif; font-size: 31px; color: var(--navy); }
  .benefits .benefit--strong { color: var(--ink); }

  .contact-rule { position: absolute; top: 677px; height: 8px; }
  .contact-rule--main { left: 0; width: 548px; background: var(--blue); }
  .contact-rule--end { left: 555px; width: 63px; background: var(--navy); }

  .phone { position: absolute; display: flex; align-items: center; gap: 14px; font-family: "Arimo", Arial, sans-serif; font-weight: 700; line-height: 1; white-space: nowrap; }
  .address { position: absolute; text-align: center; font-family: "Arimo", Arial, sans-serif; line-height: 1.15; white-space: nowrap; }
  .flyer--classic .phone { left: 96px; top: 698px; font-size: 46px; color: var(--ink); }
  .flyer--classic .address { left: 0; width: 618px; top: 755px; font-size: 19px; color: var(--ink); }

  .offer { position: absolute; left: 0; background: var(--yellow); color: var(--red); font-family: "Arimo", Arial, sans-serif; font-weight: 700; text-align: center; white-space: nowrap; }
  .flyer--classic .offer { top: 808px; width: 618px; height: 65px; font-size: 26px; line-height: 65px; }

  /* Modern variant */
  .flyer--modern .title { left: 36px; top: 28px; font-size: 74px; transform: scaleX(1.07); }
  .flyer--modern .subtitle { left: 32px; top: 108px; font-size: 29px; letter-spacing: 2px; }
  .flyer--modern .rule { left: 0; top: 146px; width: 510px; }
  .flyer--modern .intro { left: 50px; top: 156px; font-size: 21px; }
  .flyer--modern .school-mark { left: 22px; top: 218px; width: 140px; }
  .flyer--modern .school-mark__dot { width: 16px; height: 16px; background: var(--red); }
  .flyer--modern .school-mark__name { font-size: 13px; color: var(--red); }
  .flyer--modern .benefits { left: 20px; top: 318px; text-align: left; transform: none; font-family: "Oswald", "Arial Narrow", sans-serif; font-weight: 600; font-size: 38px; color: var(--navy); letter-spacing: -.5px; }
  .flyer--modern .benefits li { line-height: 1.08; }

  .dark-band { position: absolute; left: 0; top: 505px; width: 510px; height: 240px; }
  .flyer--modern .phone { left: 70px; top: 555px; font-size: 38px; color: var(--paper); }
  .flyer--modern .address { left: 0; width: 510px; top: 610px; font-size: 17px; color: var(--paper); }
  .flyer--modern .offer { top: 687px; width: 510px; height: 58px; font-size: 23px; line-height: 58px; }
</style>
</head>
<body>
<main class="canvas">

  <section class="flyer flyer--classic" aria-label="Wing Chun flyer, classic layout">
    <div class="photo photo--instructor" role="img" aria-label="Photo of a smiling instructor in a white gi with a black belt, arms folded"></div>
    <h1 class="title">WING CHUN</h1>
    <p class="subtitle">KUNG FU CLASSES</p>
    <div class="rule"></div>
    <p class="intro">INTRODUCTION CLASSES</p>
    <div class="school-mark">
      <span class="school-mark__dot"></span>
      <span class="school-mark__name">Hollin Ridge Martial Arts</span>
    </div>
    <ul class="benefits">
      <li>GET FIT</li>
      <li>MAKE NEW FRIENDS</li>
      <li>LEARN A MARTIAL ART</li>
      <li class="benefit--strong">IMPROVE SELF-CONFIDENCE</li>
    </ul>
    <div class="contact-rule contact-rule--main"></div>
    <div class="contact-rule contact-rule--end"></div>
    <p class="phone">
      <svg width="58" height="40" viewBox="0 0 58 40" aria-hidden="true"><path fill="currentColor" d="M4 14 Q29 -2 54 14 L50 22 L40 18 L40 12 Q29 8 18 12 L18 18 L8 22 Z M14 22 L44 22 L50 38 L8 38 Z"/><circle cx="29" cy="30" r="5" fill="#fff"/></svg>
      079 46081 572
    </p>
    <p class="address">Hollin Ridge Martial Arts Ground Floor<br>The Forge Thistlecombe Road Brackenmoor QX47 2TN</p>
    <p class="offer">Bring this flyer in for a FREE WEEK!</p>
  </section>

  <section class="flyer flyer--modern" aria-label="Wing Chun flyer, modern layout">
    <div class="photo photo--pair" role="img" aria-label="Photo of a female and a male student in white gis, smiling"></div>
    <h2 class="title">WING CHUN</h2>
    <p class="subtitle">KUNG FU CLASSES</p>
    <div class="rule"></div>
    <p class="intro">INTRODUCTION CLASSES</p>
    <div class="school-mark">
      <span class="school-mark__dot"></span>
      <span class="school-mark__name">Tall Reed Kung Fu</span>
    </div>
    <ul class="benefits">
      <li>GET FIT</li>
      <li>MAKE NEW FRIENDS</li>
      <li>LEARN A MARTIAL ART</li>
      <li class="benefit--strong">IMPROVE SELF-CONFIDENCE</li>
    </ul>
    <svg class="dark-band" viewBox="0 0 510 240" preserveAspectRatio="none" aria-hidden="true">
      <defs>
        <linearGradient id="bandShade" x1="0" y1="0" x2="0" y2="1">
          <stop offset="0" stop-color="#3a3a3a"/>
          <stop offset="1" stop-color="#0d0d0d"/>
        </linearGradient>
      </defs>
      <path d="M0 30 Q250 -10 510 10 L510 240 L0 240 Z" fill="var(--navy)"/>
      <path d="M0 55 Q250 15 510 30 L510 240 L0 240 Z" fill="url(#bandShade)"/>
    </svg>
    <p class="phone">
      <svg width="48" height="34" viewBox="0 0 58 40" aria-hidden="true"><path fill="currentColor" d="M4 14 Q29 -2 54 14 L50 22 L40 18 L40 12 Q29 8 18 12 L18 18 L8 22 Z M14 22 L44 22 L50 38 L8 38 Z"/><circle cx="29" cy="30" r="5" fill="#222"/></svg>
      079 46081 572
    </p>
    <p class="address">Hollin Ridge Martial Arts Ground Floor<br>The Forge Thistlecombe Road Brackenmoor QX47 2TN</p>
    <p class="offer">Bring this flyer in for a FREE WEEK!</p>
  </section>

</main>
</body>
</html>
```